Brenton High 20 year Reunion Memorial

I need a tasteful memorial poster with the names of those alumni that have deceased. The school colors are black, orange, silver and white. I would definately like the background to be black. At the top of the poster I would like it to read:
Brenton Hight School Class of 1993.
This evening is dedicated in memory of
(followed by the names on the attached file

Industry/Entity Type

School

Requirements
Must have
• Black background

```html
<!DOCTYPE html>
<html lang="en">
<head>
<meta charset="utf-8">
<title>Brenton High School Class of 1993 – Memorial</title>
<link rel="stylesheet" href="https://fonts.googleapis.com/css2?family=Marcellus&family=Barlow+Semi+Condensed:wght@500&family=Barlow:wght@700&display=swap">
<style>
  :root {
    --bg: #000000;
    --orange: #f7941d;
    --silver: #8f8f8f;
    --silver-light: #8a8a8a;
    --figure-bronze: #7a6440;
    --figure-mid: #4a3a22;
    --cape-red: #3e0a07;
  }
  * { margin: 0; padding: 0; box-sizing: border-box; }
  html, body { width: 1000px; height: 1200px; overflow: hidden; background: var(--bg); }
  .poster { position: relative; width: 1000px; height: 1200px; background: var(--bg); overflow: hidden; }

  .school-name {
    position: absolute; top: 50px; left: 0; width: 1000px; text-align: center;
    font-family: "Marcellus", serif; font-weight: 400; font-size: 62px;
    text-transform: uppercase; letter-spacing: 4px; word-spacing: 16px;
    color: var(--orange); line-height: 1;
  }
  .class-year {
    position: absolute; top: 112px; right: 108px;
    font-family: "Barlow Semi Condensed", sans-serif; font-weight: 500;
    font-size: 40px; color: var(--orange); line-height: 1;
  }
  .guardian-figure {
    position: absolute; left: 470px; top: 185px; width: 530px; height: 960px;
  }
  .dedication {
    position: absolute; top: 258px; left: 10px; width: 655px; text-align: center;
    font-family: "Marcellus", serif; font-weight: 400; font-size: 41px;
    text-transform: uppercase; letter-spacing: 2px;
    color: var(--silver-light); line-height: 50px;
  }
  .memorial-list {
    position: absolute; top: 448px; left: 35px; width: 500px; list-style: none; text-align: center;
  }
  .memorial-entry { height: 82.5px; }
  .memorial-name {
    display: block; font-family: "Barlow", sans-serif; font-weight: 700;
    font-size: 29px; color: var(--orange); line-height: 36px; letter-spacing: 0.5px;
  }
  .memorial-dates {
    display: block; font-family: "Barlow Semi Condensed", sans-serif; font-weight: 500;
    font-size: 30px; color: var(--silver); line-height: 32px;
  }
</style>
</head>
<body>
<main class="poster">
  <h1 class="school-name">Brenton High School</h1>
  <p class="class-year">Class of 1993</p>

  <svg class="guardian-figure" viewBox="0 0 530 960" role="img" aria-label="Illustration of a bronze ancient warrior with helmet, red cape, round shield and spear">
    <defs>
      <radialGradient id="bronzeGlow" cx="52%" cy="48%" r="58%" fx="50%" fy="40%">
        <stop offset="0%" stop-color="var(--figure-bronze)"/>
        <stop offset="40%" stop-color="var(--figure-mid)"/>
        <stop offset="72%" stop-color="var(--cape-red)"/>
        <stop offset="100%" stop-color="var(--bg)"/>
      </radialGradient>
    </defs>
    <rect width="530" height="960" fill="url(#bronzeGlow)"/>
  </svg>

  <h2 class="dedication">This evening is dedicated<br>in memory of</h2>

  <ul class="memorial-list">
    <li class="memorial-entry"><span class="memorial-name">Carla Jensen</span><span class="memorial-dates">May 7, 1975 - November 28, 1993</span></li>
    <li class="memorial-entry"><span class="memorial-name">Derek Lowe</span><span class="memorial-dates">April 29, 1975 -June 10, 1997</span></li>
    <li class="memorial-entry"><span class="memorial-name">Mason Reed</span><span class="memorial-dates">April 22, 1975 - April 2, 2002</span></li>
    <li class="memorial-entry"><span class="memorial-name">Luis Navarro</span><span class="memorial-dates">August 28, 1975 - February 27, 2010</span></li>
    <li class="memorial-entry"><span class="memorial-name">Tessa Lindqvist</span><span class="memorial-dates">July 13, 1975 - October 5, 2011</span></li>
    <li class="memorial-entry"><span class="memorial-name">Holly Brennan</span><span class="memorial-dates">January 26, 1975 - December 22, 2012</span></li>
    <li class="memorial-entry"><span class="memorial-name">Grant Keller</span><span class="memorial-dates">April 29, 1975 - January 30, 2013</span></li>
  </ul>
</main>
</body>
</html>
```